Business Card for my Photography/Video Business

I would like the card to say Event Photographer and Videographer. I like the Black and Gold look to it as well but open to other options. I don't want it to be super vibrant or colorful. Simple, elegant and professional

```html
<!DOCTYPE html>
<html lang="en">
<head>
<meta charset="utf-8">
<title>Loma Visuals – Business Card</title>
<link rel="stylesheet" href="https://fonts.googleapis.com/css2?family=Montserrat:wght@400;500;600&display=swap">
<style>
  :root {
    --stage: #2a2a2a;
    --black: #0b0b0b;
    --gold: #e2b325;
    --gold-light: #f2cf4a;
    --gold-deep: #b8860f;
    --gold-text: #d9ab2a;
    --muted: #b89a45;
    --card-w: 620px;
    --card-h: 354px;
    --radius: 22px;
  }
  * { box-sizing: border-box; margin: 0; padding: 0; }
  html, body {
    width: 1200px; height: 997px; overflow: hidden;
    background: var(--stage);
    font-family: "Montserrat", sans-serif;
  }
  .stage {
    width: 1200px; height: 997px;
    display: flex; flex-direction: column;
    align-items: center; justify-content: center; gap: 64px;
  }
  .card {
    position: relative;
    width: var(--card-w); height: var(--card-h);
    border-radius: var(--radius);
    overflow: hidden;
    box-shadow: 0 14px 30px rgba(0,0,0,.55);
  }
  .brand-name {
    font-weight: 500; font-size: 44px; letter-spacing: 0;
    line-height: 1; white-space: nowrap;
  }

  /* Back of card */
  .card--back { background: var(--black); }
  .card--back .band {
    position: absolute; left: 0; right: 0; height: 64px;
    background: linear-gradient(90deg, var(--gold-deep), var(--gold) 40%, var(--gold-light) 70%, var(--gold));
  }
  .card--back .band--top { top: 0; }
  .card--back .band--bottom { bottom: 0; }
  .card--back .brand-name {
    position: absolute; left: 60px; top: 112px;
    color: var(--gold-text);
  }
  .contact {
    position: absolute; left: 60px; bottom: 92px;
    list-style: none; display: flex; flex-wrap: wrap; gap: 8px 28px;
    font-size: 13px; color: var(--muted); letter-spacing: .5px;
    width: 480px;
  }
  .contact li { display: flex; align-items: center; gap: 7px; }
  .contact svg { width: 11px; height: 11px; fill: var(--muted); }

  /* Front of card */
  .card--front {
    background: radial-gradient(ellipse at 55% 45%, var(--gold-light), var(--gold) 55%, var(--gold-deep) 100%);
  }
  .card--front .band {
    position: absolute; left: 0; right: 0; background: var(--black);
  }
  .card--front .band--top { top: 0; height: 38px; }
  .card--front .band--bottom { bottom: 0; height: 92px; }
  .card--front .brand-name {
    position: absolute; left: 60px; top: 124px;
    color: var(--black);
  }
  .tagline {
    position: absolute; left: 40px; bottom: 30px;
    font-weight: 600; font-size: 28px; color: var(--gold-text); letter-spacing: .5px;
    white-space: nowrap;
  }
</style>
</head>
<body>
<main class="stage">
  <section class="card card--back" aria-label="Business card back">
    <div class="band band--top"></div>
    <p class="brand-name">Loma Visuals</p>
    <ul class="contact">
      <li><svg viewBox="0 0 24 24"><path d="M6.6 10.8a15 15 0 0 0 6.6 6.6l2.2-2.2a1 1 0 0 1 1-.25 11.4 11.4 0 0 0 3.6.57 1 1 0 0 1 1 1V20a1 1 0 0 1-1 1A17 17 0 0 1 3 4a1 1 0 0 1 1-1h3.5a1 1 0 0 1 1 1c0 1.25.2 2.45.57 3.57a1 1 0 0 1-.25 1z"/></svg>1300 555 019</li>
      <li><svg viewBox="0 0 24 24"><path d="M2 5h20v14H2z"/></svg>info@lomavisuals.com</li>
      <li><svg viewBox="0 0 24 24"><circle cx="12" cy="12" r="10"/></svg>www.lomavisuals.com</li>
    </ul>
    <div class="band band--bottom"></div>
  </section>

  <section class="card card--front" aria-label="Business card front">
    <div class="band band--top"></div>
    <p class="brand-name">Loma Visuals</p>
    <div class="band band--bottom"></div>
    <p class="tagline">Event Photographer &amp; Videographer</p>
  </section>
</main>
</body>
</html>
```